Acupuncture Medspa needs a business card design

I need a business card design that looks professional, has a spa-like quality and can offer a promo on the back. Initial promo is "First session free". The tagline of NeedleNook is: Refresh, Restore, Rejuvenate.

NeedleNook is a membership-based acupuncture medspa that offers acupuncture, cupping, and herbal therapies. Members choose between the "Refresh" membership which is for stress relief, or "Restore" which is for treating health conditions, and lastly "Rejuvenate" which is for natural facial enhancement.

Industry/Entity Type

Health And Wellness

Contact Information for Business Card

Coral Haskins, MAC, L.Ac.
612-555-0193
www.needlenook-example.com

Font styles to use
Serif
Sans Serif

Colors

Designer to choose colors to be used in the design.

Requirements
Must have
• The project must have NeedleNook logo, promo on the back, and contact information
Nice to have
• I would like to see the colors of the logo used.

```html
<!DOCTYPE html>
<html lang="en">
<head>
<meta charset="utf-8">
<title>NeedleNook Business Card</title>
<link href="https://fonts.googleapis.com/css2?family=Quicksand:wght@300;400;500&family=Montserrat:wght@500;600&display=swap" rel="stylesheet">
<style>
  :root {
    --backdrop: #7087a4;
    --card: #d4cbab;
    --magenta: #ff00ff;
    --magenta-soft: #f39cf3;
    --plum: #a0209f;
    --teal: #2f7f7d;
    --teal-pale: #9fb6a6;
    --ink: #111111;
    --tagline: #f6e9f6;
  }
  * { margin: 0; padding: 0; box-sizing: border-box; }
  html, body { width: 1200px; height: 1200px; overflow: hidden; }
  body {
    background: var(--backdrop);
    position: relative;
    font-family: "Quicksand", sans-serif;
  }
  .card {
    position: absolute;
    left: 300px;
    width: 600px;
    height: 342px;
    background: var(--card);
    overflow: hidden;
  }
  .card--front { top: 234px; }
  .card--back { top: 624px; }
  .card > svg { position: absolute; inset: 0; }

  .brand-mark {
    position: absolute;
    left: 84px; top: 70px;
    width: 192px; height: 192px;
    border: 4px solid var(--teal);
    border-radius: 50%;
    display: flex; align-items: center; justify-content: center;
  }
  .brand-name {
    font-family: "Montserrat", sans-serif;
    font-weight: 600;
    color: var(--teal);
  }
  .brand-mark .brand-name { font-size: 22px; }

  .tagline {
    position: absolute;
    left: 392px; top: 146px;
    display: flex; align-items: center;
    color: var(--tagline);
    font-weight: 300;
  }
  .tagline__initial { font-size: 92px; line-height: 1; margin-right: 2px; }
  .tagline__words { font-size: 20px; line-height: 27px; }

  .website {
    position: absolute;
    left: 100px; width: 295px; top: 300px;
    text-align: right;
    color: var(--magenta);
    font-size: 18px;
    font-weight: 400;
    white-space: nowrap;
  }

  .back-heading {
    position: absolute;
    left: 0; width: 600px; top: 62px;
    text-align: center;
  }
  .back-heading .brand-name { font-size: 36px; text-transform: uppercase; letter-spacing: 1px; }
  .promo {
    position: absolute;
    left: 0; width: 600px; top: 112px;
    text-align: center;
    color: var(--plum);
    font-size: 30px;
    font-weight: 400;
  }
  .contact {
    position: absolute;
    right: 26px; top: 176px;
    text-align: right;
  }
  .contact__name {
    font-family: "Montserrat", sans-serif;
    font-weight: 600;
    font-size: 26px;
    color: var(--ink);
    letter-spacing: -0.5px;
  }
  .contact__credentials {
    display: flex; justify-content: flex-end; align-items: center;
    color: var(--teal);
    font-size: 17px;
    margin-top: 2px;
  }
  .contact__bar {
    width: 80px; height: 13px;
    background: linear-gradient(90deg, rgba(47,127,125,0), var(--teal));
    margin-right: 2px;
  }
  .contact__phone {
    display: flex; justify-content: flex-end; align-items: center;
    gap: 12px;
    margin-top: 26px;
    font-size: 20px;
    color: var(--ink);
  }
</style>
</head>
<body>

<section class="card card--front">
  <svg width="600" height="342" viewBox="0 0 600 342" role="img" aria-label="Magenta panel holding a woman's profile silhouette">
    <path d="M330 0 C304 60 324 160 344 200 C359 240 374 265 386 280 C404 300 419 320 430 342 L600 342 L600 0 Z" fill="var(--magenta-soft)"/>
    <path d="M338 0 C312 60 332 160 352 200 C367 240 382 265 394 280 C412 300 427 320 438 342 L600 342 L600 0 Z" fill="var(--magenta)"/>
  </svg>
  <div class="brand-mark"><span class="brand-name">NeedleNook</span></div>
  <div class="tagline">
    <span class="tagline__initial">R</span>
    <span class="tagline__words">efresh<br>estore<br>ejuvenate</span>
  </div>
  <p class="website">www.needlenook-example.com</p>
</section>

<section class="card card--back">
  <svg width="600" height="342" viewBox="0 0 600 342" aria-hidden="true">
    <circle class="faint-ring" cx="106" cy="256" r="100" fill="none" stroke="var(--teal-pale)" stroke-width="4"/>
  </svg>
  <div class="back-heading"><span class="brand-name">NeedleNook</span></div>
  <p class="promo">First session free</p>
  <div class="contact">
    <p class="contact__name">Coral Haskins</p>
    <p class="contact__credentials"><span class="contact__bar"></span>MAC, L.Ac.</p>
    <p class="contact__phone">
      <svg class="phone-icon" width="16" height="16" viewBox="0 0 24 24" aria-hidden="true">
        <path fill="var(--ink)" d="M6.6 10.8a15.1 15.1 0 0 0 6.6 6.6l2.2-2.2c.3-.3.7-.4 1-.2 1.1.4 2.3.6 3.6.6.6 0 1 .4 1 1V20c0 .6-.4 1-1 1A17 17 0 0 1 3 4c0-.6.4-1 1-1h3.5c.6 0 1 .4 1 1 0 1.3.2 2.5.6 3.6.1.3 0 .7-.2 1z"/>
      </svg>
      612-555-0193
    </p>
  </div>
</section>

</body>
</html>
```